Rebranding Website – Brookvale Clinic for Herbal Care (40 Years)

Organization Description:
The Brookvale Clinic for Herbal Care (BCHC / www.bchc-example.nl) has been a trusted address for more than 40 years for people who choose a natural and sustainable approach to their health. We combine experience and history with a modern, professional approach.

Assignment:
Our current website is outdated and no longer reflects who we are today. We are looking for a new web design that aligns with our renewed logo and is both functional and inspiring. The website should have a clear structure, be user-friendly, and convey trust.

What we are looking for in the design:

A modern, fresh look that matches our logo and color palette logo in attachment.

Goal-oriented: simple and intuitive appointment scheduling.

Informative: space for a blog/news section to share knowledge and updates.

A dedicated page for each therapist with photo, expertise, and contact options.

A separate page for each type of therapy, with explanations and benefits.

A clear and visible link to our webshop (separate website).

Clear navigation and an organized menu structure.

Responsive design (desktop, tablet, mobile).

User-friendly CMS so we can manage and expand content ourselves.

Style Preferences:

- Color palette in line with our logo (green and natural tones, complemented by fresh and calm accents).
- Clean, professional design with plenty of white space.
- Accessible, warm, and inviting.

Functionalities:
- Online appointment scheduling or easy contact options.
- Blog/news section.
- Dedicated pages for therapists and therapies.
- Link to webshop.
- Possibility to expand the offer in the future (e.g., videos, downloads, or e-consultations).

What we would like to avoid:
- Pages that are too cluttered or confusing.
- Excessive text without clear structure.
- Stock photos lacking authenticity.

Target Audience:
People who consciously focus on their health, choose a natural approach, and are looking for a professional and reliable center where expertise and personal attention are central.

Additional Information:
The new website should bridge our 40-year history with the future. A place where visitors feel both familiar and inspired – and where they are immediately invited to get in touch, book an appointment, or visit our webshop.

You find our logo and impression in the uploads.

```html
<!DOCTYPE html>
<html lang="en">
<head>
<meta charset="utf-8">
<title>Brookvale Clinic for Herbal Care</title>
<link rel="stylesheet" href="https://fonts.googleapis.com/css2?family=Lora:wght@400;600;700&family=Montserrat:wght@600;700&display=swap">
<style>
:root{
  --green-dark:#4a5e2a;
  --green-text:#4f6328;
  --lime:#8cc63f;
  --lime-deep:#7bb52e;
  --ink:#3a3f36;
  --wash:#eef6dd;
  --wash-soft:#f5faea;
  --white:#ffffff;
  --line:#e6e9e2;
}
*{box-sizing:border-box;margin:0;padding:0}
html,body{width:1200px;height:960px;overflow:hidden;background:var(--white)}
body{position:relative;font-family:"Lora",Georgia,serif;color:var(--ink)}
.backdrop{position:absolute;inset:0;z-index:0}
.site-header{position:absolute;top:0;left:0;width:1200px;height:82px;background:var(--white);border-bottom:1px solid var(--line);z-index:3}
.brand{position:absolute;left:22px;top:18px;display:flex;align-items:center;gap:8px;text-decoration:none}
.brand-dot{width:46px;height:46px;border-radius:50%;border:3px solid var(--lime);display:flex;align-items:center;justify-content:center}
.brand-name{font-family:"Lora",Georgia,serif;font-weight:700;font-size:13px;color:var(--green-dark)}
.main-nav{position:absolute;left:222px;top:29px;display:flex;gap:31px}
.main-nav a{font-size:16.5px;color:var(--ink);text-decoration:none}
.webshop-link{position:absolute;left:876px;top:29px;font-size:16.5px;font-weight:700;color:var(--green-text);text-decoration:none}
.btn{display:inline-flex;align-items:center;justify-content:center;font-family:"Montserrat",Arial,sans-serif;font-weight:700;color:var(--white);background:linear-gradient(180deg,var(--lime),var(--lime-deep));border-radius:5px;text-decoration:none;box-shadow:0 6px 14px rgba(122,180,46,.3)}
.btn-header{position:absolute;left:987px;top:21px;width:177px;height:41px;font-size:14.5px}
.hero{position:absolute;left:22px;top:185px;width:640px;z-index:2}
.hero-badge{width:143px;height:165px;border-radius:50%;background:var(--white);box-shadow:0 10px 30px rgba(0,0,0,.1);display:flex;align-items:center;justify-content:center;gap:8px}
.hero-badge .badge-ring{width:18px;height:18px;border-radius:50%;border:3px solid var(--lime)}
.hero-badge span{font-family:"Lora",Georgia,serif;font-weight:700;font-size:26px;color:var(--green-dark)}
.hero-title{margin-top:52px;font-family:"Montserrat",Arial,sans-serif;font-weight:700;font-size:60px;line-height:57px;color:var(--green-dark);letter-spacing:-.3px}
.hero-lead{margin-top:24px;font-size:20.5px;line-height:28px;color:var(--ink);width:640px}
.btn-hero{margin-top:42px;width:272px;height:56px;font-size:18px}
</style>
</head>
<body>
<svg class="backdrop" width="1200" height="960" viewBox="0 0 1200 960" aria-hidden="true">
  <defs>
    <linearGradient id="panel" x1="0" y1="0" x2="1" y2="1">
      <stop offset="0" stop-color="#e9f5d3"/>
      <stop offset="1" stop-color="#f4f9ea"/>
    </linearGradient>
  </defs>
  <rect width="1200" height="960" fill="#ffffff"/>
  <circle cx="240" cy="760" r="300" fill="#f6f8f3"/>
  <polygon points="630,82 1188,82 1188,948 533,948" fill="url(#panel)"/>
  <circle cx="980" cy="330" r="300" fill="#e6f3cc" opacity=".5"/>
  <path d="M0,900 C300,860 700,930 1200,890 L1200,960 L0,960 Z" fill="#f7f9f5"/>
  <rect x="1188" y="82" width="12" height="878" fill="#f1f1f1"/>
  <rect x="1190" y="90" width="8" height="70" rx="4" fill="#c4c4c4"/>
</svg>

<header class="site-header">
  <a class="brand" href="#"><span class="brand-dot"><span class="brand-name">BCHC</span></span></a>
  <nav class="main-nav">
    <a href="#">Home</a>
    <a href="#">About Us</a>
    <a href="#">Therapies</a>
    <a href="#">Team</a>
    <a href="#">Knowledge</a>
    <a href="#">Contact</a>
  </nav>
  <a class="webshop-link" href="#">Our Webshop</a>
  <a class="btn btn-header" href="#">Book Appointment</a>
</header>

<section class="hero">
  <div class="hero-badge"><span class="badge-ring"></span><span>BCHC</span></div>
  <h1 class="hero-title">Your Path to Natural<br>Wellness</h1>
  <p class="hero-lead">Backed by 40 years of trust, we combine modern science with natural therapies for a healthy and sustainable lifestyle.</p>
  <a class="btn btn-hero" href="#">Book an Appointment</a>
</section>
</body>
</html>
```